Can You Help Sell Glass Cabinets with a Banner Ad?

Our New Zealand-based company designs and sells glass cabinets and display cases. 75% of our customers are other businesses who want to display products in their shop or showroom. The other 25% of our customers are householders who want a glass cabinet for their personal collectables. We have been trading 2 years now, and are expanding rapidly. Our website address is www.vitrinaplace.example.nz.
We have made a strategic decision to focus on online advertising this year. This is because we want to raise our profile to the greatest number of and widest range of people. For now, this means banner advertising on high traffic New Zealand-based websites in an attempt to generate more traffic to our website. The websites we will initially use are www.ploverpost.example.nz and www.tuidaily.example.nz.
We therefore need a set of eye-catching banner ads designed for our online marketing campaign. The three banners required will probably just be variations on a single design.

Banner 1: Top Banner
760x120

Banner 2: Skyscraper
160x600

Banner 3: Medium Rectangle
300x250

Target Market(s)

The primary target market will be retailers who have shops and showrooms. They may not yet know they need a showcase.

Industry/Entity Type

Advertising

Requirements
Must have
• Vitrina Place logo
"High quality glass cabinets and showcases"
Maybe also "Show your products, not the cabinet"
[Corporate colour is green, as per logo. Secondary colours are orange, purple and grey.]
[Please use New Zealand (British) spelling]

Nice to have
• Please view our website and brochure on the Resources page for the look and feel of our company. In particular we like our logo, so it is possible you can take a lead from this. The logo emblem is designed to be evocative of glass.
The logo spot colour is 41,0,70,10.

```html
<!DOCTYPE html>
<html lang="en-NZ">
<head>
<meta charset="utf-8">
<title>Vitrina Place — Top Banner</title>
<link rel="stylesheet" href="https://fonts.googleapis.com/css2?family=Arimo:wght@400;700&display=swap">
<style>
  :root {
    --ink: #111111;
    --body-grey: #3a3a3a;
    --purple: #9a7dbd;
    --orange: #e8963a;
    --brand-green: #8cbf5e;
    --white: #ffffff;
    --paper: #ffffff;
  }
  html, body {
    margin: 0;
    padding: 0;
    width: 1200px;
    height: 189px;
    overflow: hidden;
    background: var(--paper);
  }
  .banner {
    display: block;
    width: 1200px;
    height: 189px;
    font-family: "Arimo", Arial, sans-serif;
  }
  .headline { fill: var(--ink); font-weight: 400; }
  .headline .accent { fill: var(--purple); }
  .strapline { fill: var(--body-grey); font-weight: 400; }
  .strapline .highlight { fill: var(--orange); }
  .brand-panel { fill: var(--brand-green); }
  .brand-square { fill: var(--white); opacity: 0.85; }
  .brand-name { fill: var(--white); font-weight: 700; }
</style>
</head>
<body>
<svg class="banner" viewBox="0 0 1200 189" xmlns="http://www.w3.org/2000/svg" role="img"
     aria-label="Vitrina Place: Show your products, not the cabinet. High quality glass cabinets and showcases.">
  <text class="headline" x="2" y="56" font-size="64"
        textLength="766" lengthAdjust="spacingAndGlyphs">SHOW YOUR PRODUCTS,</text>

  <text class="headline" x="2" y="133" font-size="94"
        textLength="730" lengthAdjust="spacingAndGlyphs">NOT THE <tspan class="accent">CABINET</tspan></text>

  <text class="strapline" x="3" y="172" font-size="33"
        textLength="745" lengthAdjust="spacingAndGlyphs">high quality <tspan class="highlight">glass cabinets</tspan> and <tspan class="highlight">showcases</tspan></text>

  <g class="brand">
    <rect class="brand-panel" x="785" y="67" width="393" height="73"/>
    <rect class="brand-square" x="805" y="84" width="38" height="38"/>
    <text class="brand-name" x="860" y="113" font-size="28">Vitrina Place</text>
  </g>
</svg>
</body>
</html>
```